flights and hotels for a great prices, really cheap... Lower Than Your Voyage

Use the Sample Flyer as in idea of what i am looking for. I would like to have the mission statement in the front of the flyer and Q&A in the back own its own, if you can put it all there. My company gives travel deals which range any where from 30% to %50 off, so if you can make something pop out this that key information. Just work your magic and surprise me with what you come up with remember i need a flyer that really points out that we can book any travel for %30 to %50.
Updates

I up loaded my logo and I do not what any people on my flyer. Added Tuesday, June 28, 2016

Project Deadline Extended Reason: I have upload my logo. Plus I seen some designers added on people to the flyers. I wanted no people on it. Added Tuesday, June 28, 2016

The IG is @LTVvoyage sorry for the "c" that was added on. Added Tuesday, June 28, 2016

Industry/Entity Type

Travel

Requirements
Must have
• Great parts of the world.
Nice to have
• What people like to see when they travel!
Should not have
• People in the background of the flyers

```html
<!DOCTYPE html>
<html lang="en">
<head>
<meta charset="utf-8">
<title>Lower Than Your Voyage – Flyer</title>
<link href="https://fonts.googleapis.com/css2?family=Lobster&family=Raleway:ital,wght@0,400;0,600;0,700;1,400&display=swap" rel="stylesheet">
<style>
  :root{
    --backdrop:#1e1e1e;
    --paper:#ececec;
    --orange:#f7911c;
    --orange-deep:#f47a20;
    --blue:#1b98d4;
    --sky:#3cbbe9;
    --navy:#0e4a68;
    --ink:#3a3a3a;
    --rule:#6fb8dc;
  }
  *{box-sizing:border-box;margin:0;padding:0}
  html,body{width:1200px;height:1200px;overflow:hidden;background:var(--backdrop)}
  .stage{position:absolute;left:0;top:0;width:1500px;height:1500px;transform:scale(.8);transform-origin:0 0;font-family:'Raleway',sans-serif;color:var(--ink)}
  .page{position:absolute;top:299px;width:696px;height:894px;overflow:hidden;
    background:linear-gradient(180deg,#e2e2e2 0%,#f1f1f1 45%,#e9e9e9 100%);box-shadow:0 4px 18px rgba(0,0,0,.5)}
  .page--front{left:41px}
  .page--back{left:761px}
  .backdrop-photo{position:absolute;inset:0;background:linear-gradient(180deg,#dcdcdc 0%,#efefef 30%,#e0e0e0 70%,#ececec 100%)}
  .collage{position:absolute;left:0;top:0;width:696px;height:540px}
  .edge-shapes{position:absolute;left:0;top:660px;z-index:0}
  .logo{position:absolute;left:506px;top:60px;display:flex;align-items:center;gap:6px}
  .logo__dot{width:18px;height:18px;border-radius:50%;background:var(--orange)}
  .logo__name{font-size:25px;font-weight:600;color:var(--navy)}
  .banner{position:absolute;left:59px;top:27px;width:430px;height:28px;color:#fff;font-size:19px;line-height:28px;text-align:center}
  .offer{position:absolute;left:119px;top:68px;width:310px;height:73px;color:#fff;font-family:'Lobster',cursive;text-align:center;line-height:33px;font-size:32px;padding-top:4px}
  .mission-title{position:absolute;z-index:1;left:29px;top:494px;font-family:'Lobster',cursive;color:var(--blue);font-size:28px}
  .mission{position:absolute;z-index:1;left:30px;top:535px;width:630px;font-size:12.9px;line-height:16.6px}
  .mission p{position:relative;padding-bottom:9px;margin-bottom:10px}
  .mission p::after{content:"";position:absolute;left:0;bottom:0;width:590px;border-bottom:1.5px dashed var(--rule)}
  .mission p:last-child::after{display:none}
  .contact-title{position:absolute;z-index:1;left:0;width:696px;top:768px;text-align:center;font-family:'Lobster',cursive;color:var(--blue);font-size:30px}
  .contact{position:absolute;z-index:1;display:flex;align-items:center;gap:22px;font-size:18px;color:#444;white-space:nowrap;border-top:1.5px dashed var(--rule);border-bottom:1.5px dashed var(--rule)}
  .contact span{display:flex;align-items:center;gap:7px;white-space:nowrap;flex:none}
  .page--front .contact{left:42px;top:824px;width:612px;height:48px;justify-content:center}
  .page--back .contact{left:36px;top:151px;width:620px;height:36px;justify-content:space-between}
  .icon{width:20px;height:20px;flex:none}
  .back-copy{position:absolute;left:39px;top:22px;width:630px;font-size:13.2px;line-height:16.6px}
  .back-copy h1{font-size:14.5px;font-weight:700;color:var(--navy);letter-spacing:.2px}
  .qa{position:absolute;left:39px;top:200px;width:640px;font-size:13.2px;line-height:16.6px}
  .qa h2{font-size:16px;font-weight:400;margin-bottom:7px;color:#333}
  .qa dt{font-style:italic}
  .qa dd{margin-bottom:10px}
  .qa small{display:block;font-size:10.6px;line-height:14.4px}
</style>
</head>
<body>
<div class="stage">

  <section class="page page--front">
    <div class="backdrop-photo" role="img" aria-label="Faded resort background photo"></div>
    <svg class="collage" viewBox="0 0 696 540" xmlns="http://www.w3.org/2000/svg">
      <polygon points="269,-59 419,91 269,241 119,91" fill="var(--orange)"/>
      <polygon points="0,20 150,170 40,280 0,240" fill="#7aa26a" role="img" aria-label="Photo of palm trees and a beach hut"/>
      <polygon points="79,241 179,341 79,441 -21,341" fill="#9aa3a8" role="img" aria-label="Photo of white seaside village houses"/>
      <polygon points="159,151 259,251 159,351 59,251" fill="#6bb3c8" role="img" aria-label="Photo of a pool with a thatched umbrella"/>
      <polygon points="399,131 489,221 399,311 309,221" fill="#b7a46a" role="img" aria-label="Photo of a noodle dish"/>
      <polygon points="639,111 719,191 639,271 559,191" fill="#7a8a4a" role="img" aria-label="Photo of a plated meal"/>
      <polygon points="299,240 449,390 299,540 149,390" fill="#4e95c4" role="img" aria-label="Photo of a leaning palm over a tropical sea"/>
      <polygon points="549,191 699,341 549,491 399,341" fill="#7fb6cf" role="img" aria-label="Photo of a resort pool with palm trees"/>
      <polygon points="497,131 542,176 497,221 452,176" fill="var(--sky)"/>
      <polygon points="679,226 724,271 679,316 634,271" fill="var(--navy)"/>
      <polygon points="166,363 226,423 166,483 106,423" fill="var(--orange-deep)"/>
      <polygon points="434,361 514,441 434,521 354,441" fill="var(--blue)"/>
      <polygon points="519,451 559,491 519,531 479,491" fill="var(--navy)"/>
      <polygon points="679,341 779,441 679,541 579,441" fill="var(--orange-deep)"/>
      <polygon points="69,27 479,27 489,41 479,55 69,55 59,41" fill="var(--navy)"/>
      <polygon points="139,68 409,68 429,104 409,141 139,141 119,104" fill="var(--navy)"/>
      <polygon points="74,37 70,41 74,45" fill="#fff"/><polygon points="474,37 478,41 474,45" fill="#fff"/>
      <polygon points="156,96 148,104 156,112" fill="var(--orange)"/><polygon points="392,96 400,104 392,112" fill="var(--orange)"/>
    </svg>
    <svg class="edge-shapes" width="696" height="150" viewBox="0 0 696 150">
      <polygon points="696,5 696,55 671,30" fill="var(--orange-deep)"/>
      <polygon points="696,60 696,130 661,95" fill="var(--navy)"/>
      <polygon points="654,85 679,110 654,135 629,110" fill="var(--blue)"/>
      <polygon points="0,60 16,76 0,92" fill="var(--navy)"/>
      <polygon points="0,95 25,120 0,145" fill="var(--orange-deep)"/>
      <polygon points="28,120 44,136 28,152 12,136" fill="var(--navy)"/>
    </svg>
    <div class="banner">Book your holiday weekend travel with us</div>
    <div class="offer">and Get Min<br>30% - 50% off</div>
    <div class="logo"><span class="logo__dot"></span><span class="logo__name">LTVoyage</span></div>

    <h2 class="mission-title">Mission Statement</h2>
    <div class="mission">
      <p>It's not something we've written down or framed on the wall. It's hardwired into each and every one of us working at Lower Than Your Voyage. We live and breathe it every day by researching, managing, organizing and negotiating the best values for airfares and hotel rates.</p>
      <p>We pass these premium values on to you, our valued customers. So you can create epic memories while optimizing your traveling experiences. Here at LTYV we believe that traveling is essential for human growth! So you're guaranteed to receive maximum value on our services for every one of your hard earned travel dollars.</p>
      <p>LTYV provides personalized, responsive travel service, based first and foremost on the travel needs of our valued clients, through meticulous attention to details, we pride ourselves in delivering, PRIME values and professional courtesy. We want to inspire our clients to explore to world and create experiences that will last a lifetime to explore the world.</p>
    </div>
    <h2 class="contact-title">Contact us for you all your travelling needs</h2>
    <div class="contact">
      <span><svg class="icon" viewBox="0 0 20 20"><rect x="5" y="1" width="10" height="18" rx="2" fill="none" stroke="var(--blue)" stroke-width="1.8"/></svg>(555) 014 LTYV (5898)</span>
      <span><svg class="icon" viewBox="0 0 20 20"><rect x="1" y="4" width="18" height="12" fill="var(--blue)"/><path d="M1 4l9 7 9-7" fill="none" stroke="#fff" stroke-width="1.3"/></svg>LTVvoyage@mailbox.test</span>
      <span><svg class="icon" viewBox="0 0 20 20"><rect x="1" y="1" width="18" height="18" fill="var(--blue)"/></svg>@LTVvoyage</span>
    </div>
  </section>

  <section class="page page--back">
    <div class="backdrop-photo" role="img" aria-label="Faded hotel pool background photo"></div>
    <div class="back-copy">
      <h1>WELCOME TO LOWER THAN YOUR VOYAGE AGENCY.</h1>
      <p>On behalf of everyone here at LTYV we thank you for taking time out of your busy schedule to book your dream vacation with us, because of such large demand for booking. We created a frequently Asked question PDF. We compiled some of the most asked questions from our customers and created this Q&amp;A. If you have a question that's not listed on the Q&amp;A don't be afraid to ask contact us by phone or email directly. We're available 24 hours/7 Days questions will be answered within 24 to 48 hours via (email), or within the hour via phone.</p>
    </div>
    <div class="contact">
      <span><svg class="icon" viewBox="0 0 20 20"><rect x="5" y="1" width="10" height="18" rx="2" fill="none" stroke="var(--blue)" stroke-width="1.8"/></svg>(555) 014 LTYV (5898)</span>
      <span><svg class="icon" viewBox="0 0 20 20"><rect x="1" y="4" width="18" height="12" fill="var(--blue)"/><path d="M1 4l9 7 9-7" fill="none" stroke="#fff" stroke-width="1.3"/></svg>LTVvoyage@mailbox.test</span>
      <span><svg class="icon" viewBox="0 0 20 20"><rect x="1" y="1" width="18" height="18" fill="var(--blue)"/></svg>@LTVvoyage</span>
    </div>
    <dl class="qa">
      <h2>QUESTIONS &amp; ANSWERS:</h2>
      <dt>Q: What is the price for your services?</dt><dd>A: 30% to 50% off the retail price. We beat our direct competitor prices.</dd>
      <dt>Q: What is the minimum amount of nights I have to book a room for?</dt><dd>A: The minimum is 2 nights.</dd>
      <dt>Q: What is the minimum retail price I can book your services for?</dt><dd>A: $1000 for hotel rooms.<br>A: $600 for one flight passenger, $800 for two flight passengers and $1,000 for 3+ flight passengers.</dd>
      <dt>Q: What is the minimum quality hotel you can book?</dt><dd>A: Minimum is 4 stars; we might do 3 stars as well depending on their price.</dd>
      <dt>Q: How far in advance can I book your services?</dt><dd>A: Up to 2 weeks in advance.</dd>
      <dt>Q: Is there a deal for package (hotel and flight)</dt><dd>A: As of right now we are not currently able to create package deals. Usually are prices still beat a few package deals!</dd>
      <dt>Q: How do I confirm a booking that has been done through you?</dt><dd>A: We'll give you the confirmation to where you can call or check online.</dd>
      <dt>Q: How long done it takes?</dt><dd>A: After the deposit is made, we will process the order which takes 7 to 10 days.</dd>
      <dt>Q: How far in advance can I cancel my booking after paying the deposit?</dt><dd>A: After deposit is received cancellation can not be expedited!! I repeat once deposit is received cancellation can not be expedited!!! Under no circumstances!!!</dd>
      <dt>Q: Do you guys have Fee's for your service?</dt><dd>A: Yes we do. Just like any respectable travel agency, there are government mandated taxes and minimal booking fee.</dd>
      <dt>Q: Do you guys have a refund policy?</dt><dd>A: Yes we do. We have two options when it comes to the refund policy. Refund will take effect if we &nbsp;are not able to book your specific booking as was agreed on when deposit is received..
        <small>Refunded options 1<br>- If for some reason we're not able to book your trip and a deposit was received. You will received 100% cash back of your deposit which can take up to 2 to 3 business days.. upon request..<br>Refunded options 2<br>- If for some reason we're not able to book your trip and a deposit was received. We may have an option to upgrade you with no extra charge to you.. Which means you'll pay the same price that was confirmed for the first booking.....</small></dd>
    </dl>
  </section>

</div>
</body>
</html>
```